Insurance company needs a business card design

We need a business card design for a Massachusetts-based insurance company Veloria Insurance, LLC. We provide auto insurance to Hispanic (Spanish- or Portuguese-speaking) immigrants in the United States. We will give these business cards to auto dealers where such customers typically go to purchase vehicles. We will provide a solution to the dealers to provide easy insurance to the customers buying cars at their dealerships. Veloria is the Spanish word for protection.
Contact Information for Business Card
Name, Designation, Company Name, Address, Phone Number, Email, Website
Look and feel
Each slider illustrates characteristics of the customer's brand and the style your logo design should communicate.

```html
<!DOCTYPE html>
<html lang="en">
<head>
<meta charset="utf-8">
<title>Veloria Insurance – Business Card</title>
<link href="https://fonts.googleapis.com/css2?family=Roboto:wght@400;700&display=swap" rel="stylesheet">
<style>
  :root {
    --backdrop: #2e2f31;
    --brand-blue: #12558c;
    --brand-blue-light: #1a6a9f;
    --brand-orange: #f0851f;
    --ink: #555a60;
    --paper: #ffffff;
    --rule: #c9ccd0;
  }
  * { margin: 0; padding: 0; box-sizing: border-box; }
  html, body { width: 1200px; height: 900px; overflow: hidden; }
  body {
    background: var(--backdrop);
    font-family: 'Roboto', Arial, sans-serif;
    display: flex;
    flex-direction: column;
    align-items: center;
    justify-content: center;
    gap: 60px;
  }
  .card {
    position: relative;
    width: 630px;
    height: 360px;
    border-radius: 18px;
    overflow: hidden;
  }
  .card-front { background: var(--paper); }
  .card-back {
    background: linear-gradient(135deg, var(--brand-blue) 0%, var(--brand-blue-light) 55%, var(--brand-blue) 100%);
    display: flex;
    align-items: center;
    justify-content: center;
  }
  .brand {
    display: flex;
    align-items: center;
    gap: 14px;
    font-weight: 700;
    letter-spacing: 2px;
    text-transform: uppercase;
  }
  .brand-square {
    width: 22px;
    height: 22px;
    background: var(--brand-orange);
  }
  .card-front .brand {
    position: absolute;
    left: 44px;
    top: 128px;
    font-size: 30px;
    color: var(--brand-blue);
    line-height: 1.1;
  }
  .card-back .brand { font-size: 40px; color: var(--paper); }
  .divider {
    position: absolute;
    left: 300px;
    top: 70px;
    width: 1px;
    height: 190px;
    background: var(--rule);
  }
  .contact {
    position: absolute;
    left: 328px;
    top: 78px;
    color: var(--ink);
    font-size: 15px;
    line-height: 1.45;
  }
  .contact-name {
    color: var(--brand-orange);
    font-size: 22px;
    font-weight: 700;
    text-transform: uppercase;
    letter-spacing: 0.5px;
  }
  .contact-role { font-size: 15px; margin-bottom: 14px; }
  .contact-address { margin-bottom: 8px; }
  .contact-line { display: flex; align-items: center; gap: 8px; }
  .contact-line svg { width: 13px; height: 13px; fill: var(--brand-blue); flex: none; }
  .footer-band { position: absolute; left: 0; bottom: 0; width: 630px; height: 60px; }
  .website {
    position: absolute;
    left: 118px;
    bottom: 12px;
    color: var(--paper);
    font-size: 15px;
  }
</style>
</head>
<body>
  <section class="card card-front">
    <div class="brand"><span class="brand-square"></span>Veloria<br>Insurance</div>
    <div class="divider"></div>
    <div class="contact">
      <div class="contact-name">Daniel Reyes</div>
      <div class="contact-role">Founder &amp; CEO</div>
      <div class="contact-address">48 Harbor Street Suite 310<br>Boston, MA, USA</div>
      <div class="contact-line">
        <svg viewBox="0 0 24 24"><path d="M6.6 10.8a15 15 0 0 0 6.6 6.6l2.2-2.2a1 1 0 0 1 1-.25 11.4 11.4 0 0 0 3.6.57 1 1 0 0 1 1 1V20a1 1 0 0 1-1 1A17 17 0 0 1 3 4a1 1 0 0 1 1-1h3.5a1 1 0 0 1 1 1c0 1.25.2 2.45.57 3.57a1 1 0 0 1-.25 1z"/></svg>
        (866) 555-0182
      </div>
      <div class="contact-line">
        <svg viewBox="0 0 24 24"><path d="M6 2h12v5H6zM4 8h16a2 2 0 0 1 2 2v6h-4v5H6v-5H2v-6a2 2 0 0 1 2-2zm4 8v3h8v-3z"/></svg>
        (866) 555-0182
      </div>
      <div class="contact-line">
        <svg viewBox="0 0 24 24"><path d="M2 5h20v14H2zm2 2v.5l8 5 8-5V7l-8 5z"/></svg>
        info@veloriainsurance.com
      </div>
    </div>
    <svg class="footer-band" viewBox="0 0 630 60" preserveAspectRatio="none" aria-hidden="true">
      <polygon points="0,48 630,48 630,60 0,60" fill="var(--brand-blue)"/>
      <polygon points="80,60 105,18 300,18 300,60" fill="var(--brand-orange)"/>
    </svg>
    <div class="website">veloriainsurance.com</div>
  </section>

  <section class="card card-back">
    <div class="brand"><span class="brand-square"></span>Veloria Insurance</div>
  </section>
</body>
</html>
```